WebHaven Sentry (Parental Guidance software) brochure

We want a brochure that gives an overview of the service that we provide which can be emailled to users at their request. Including the front cover it should be 4-5 pages in length. The website https://www.webhavensentry.co.uk describes our service.
The industry terms our app Parental Control but we call it Parental Guidance so we don't want the term Parental Control on here.

We can provide the text that can go into the brochure. The design should be informal but informative. We are also a member of the NCB and DSR so we need to include logos in the brochure somewhere.

Target Market(s)

The target market is parents who are visiting the website, this will be a downloadable brochure.

Industry/Entity Type

Information Technology

Requirements
Must have
• The front of the brochure should be a cover page with images and the words "Parental Guidance with WebHaven Sentry"
• The second page should have some text about the service and a small piece about the company behind it, Marlow IT Ltd and some of the main features of the service i.e. what it can do including some screenshots.
• The third page would have statistics such as
• Page 3
• Statistics page –
• 1 in 3 Internet users are children.
• 1 in 5 eight to eleven-year olds have a social media profile.
• 1 in 3 children have been a victim of cyberbullying.
• By 15 years old 65% of children have seen online pornography. Children were most likely to see it via pop-ups than by searching for it.
• Just over half of boys (53%) who had seen pornography thought it was ‘realistic’.
• One in three parents (33%) claims to filter their child’s internet use and one in four (27%) uses monitoring software.
• Overall, only a quarter of children (27%) and a third of parents think parents are effective in helping to keep children safe online.
• The fourth page would give details of facebook and twitter pages, what support we provide (currently email based), as details of future features.
Should not have
• Images from the website...The brochure should be individual to the website as people will be requesting it from the website.
• Should not have the term Parental Control, but can use Parental Guidance

```html
<!DOCTYPE html>
<html lang="en">
<head>
<meta charset="utf-8">
<title>WebHaven Sentry – Parental Guidance brochure</title>
<link href="https://fonts.googleapis.com/css2?family=Montserrat:wght@300;600;700&family=Oswald:wght@400;500&family=Roboto+Condensed:wght@300;400;700&display=swap" rel="stylesheet">
<style>
:root{
  --backdrop:#4a4a4c;
  --paper:#ffffff;
  --blue:#3aa3db;
  --blue-soft:#8ccbed;
  --teal:#0d4b62;
  --ink:#2c2c2c;
  --grey:#6b6b6b;
  --rule:#d4d4d4;
  --faint:#f0f0f0;
}
*{margin:0;padding:0;box-sizing:border-box}
html,body{width:1163px;height:1200px;overflow:hidden}
body{background:var(--backdrop);position:relative;font-family:"Roboto Condensed",sans-serif;color:var(--ink)}
.page{position:absolute;width:357px;height:504px;background:var(--paper);overflow:hidden}
.page--cover{left:185px;top:67px}
.page--features{left:621px;top:67px}
.page--stats{left:185px;top:628px}
.page--back{left:621px;top:628px}
.abs{position:absolute}

/* brand */
.brand{display:flex;align-items:center;gap:6px;color:var(--teal);font-family:"Montserrat",sans-serif;font-weight:700}
.brand__dot{width:16px;height:16px;border-radius:50%;background:var(--blue)}

/* cover */
.cover-brand{left:0;right:0;top:30px;justify-content:center;font-size:17px}
.cover-arcs{left:0;top:0;width:357px;height:504px}
.cover-photo{left:59px;top:82px;width:244px;height:302px;
  background:linear-gradient(160deg,#d9dde2 0%,#c7b39f 35%,#8aa6c3 65%,#e6e1dc 100%);
  clip-path:polygon(50% 0,100% 14%,100% 55%,85% 80%,50% 100%,15% 80%,0 55%,0 14%)}
.cover-title{left:20px;top:410px;font-family:"Montserrat",sans-serif;font-weight:700;line-height:1}
.cover-title__a{color:var(--blue);font-size:14px;margin-left:8px}
.cover-title__b{color:var(--teal);font-size:21px;margin:3px 0 3px 20px}
.cover-title__c{color:var(--blue);font-size:11px;margin-left:0}
.footer-line{left:0;width:357px;height:1px;background:var(--blue-soft)}
.footer-url{right:17px;font-size:6.5px;color:var(--ink);display:flex;align-items:center;gap:2px}
.footer-url::before{content:"";width:5px;height:5px;border-radius:50%;background:var(--blue)}

/* ribbon */
.ribbon{height:38px;background:var(--blue);color:#fff;font-family:"Montserrat",sans-serif;line-height:1;padding:10px 0 0 14px}
.ribbon__light{font-weight:300;font-size:10px;display:block;border-left:1px solid #fff;padding-left:3px}
.ribbon__bold{font-weight:700;font-size:10.5px;display:block;border-left:1px solid #fff;padding-left:3px}
.ribbon--right{left:182px;width:175px;top:31px;height:48px;padding-top:13px;padding-left:43px;
  clip-path:polygon(0 0,100% 0,100% 100%,0 100%,22px 50%)}
.ribbon--right .ribbon__light,.ribbon--right .ribbon__bold{font-size:11.5px}
.ribbon--left{left:0;width:140px;top:33px;clip-path:polygon(0 0,88% 0,100% 50%,88% 100%,0 100%)}

/* features */
.feature{width:138px;text-align:center}
.feature__icon{display:block;margin:0 auto 3px;height:18px}
.feature__title{font-weight:700;font-size:6.6px;text-transform:uppercase;margin-bottom:2px}
.feature__text{font-size:5.2px;line-height:1.55;color:var(--ink);text-align:justify}
.feature--center .feature__text{text-align:center}
.features-photo{left:0;top:283px;width:357px;height:221px;
  background:linear-gradient(90deg,#cbb8a1 0%,#d8c7b2 35%,#e8e2da 65%,#fbfbfa 90%,#ffffff 100%)}
.features-photo::after{content:"";position:absolute;inset:0;background:linear-gradient(180deg,#ffffff 0%,rgba(255,255,255,0) 25%)}

/* stats */
.stat-rule{height:1px;background:var(--rule);left:48px;width:256px}
.stat-axis{left:176px;top:153px;width:1px;height:305px;background:var(--rule)}
.stat-knot{width:10px;height:10px;border-radius:50%;background:#cfcfcf;left:171px}
.stat{width:130px;text-align:center;color:var(--grey);font-size:6.4px;line-height:1.35}
.stat__num{font-family:"Oswald",sans-serif;font-size:14px;color:#555;line-height:1.1}
.stat__icon{display:block;margin:0 auto 2px}
.stat-hero{left:83px;top:100px;display:flex;align-items:center;gap:10px}
.stat-hero .stat__num{font-size:15px}
.stat-hero p{font-size:7px;color:var(--grey);line-height:1.3}

/* back */
.back-mark{left:26px;top:20px;width:300px;height:230px;border-radius:50%;background:var(--faint)}
.back-brand{left:0;right:0;top:316px;justify-content:center;font-size:15px}
.back-support{left:0;right:0;top:378px;text-align:center}
.back-support h2{font-family:"Montserrat",sans-serif;font-size:9px;font-weight:300;color:var(--ink)}
.back-support h2 b{font-weight:600}
.contacts{display:flex;justify-content:center;gap:12px;font-size:6px;margin-top:2px}
.contacts span::before{content:"";display:inline-block;width:3px;height:3px;background:var(--blue);margin-right:2px;vertical-align:middle}
.socials{display:flex;justify-content:center;gap:4px;margin-top:4px}
.socials i{width:9px;height:9px;border-radius:50%;background:var(--blue)}
.back-rule{left:41px;width:275px;top:428px;height:1px;background:var(--blue-soft)}
.members{left:0;right:0;top:446px;text-align:center;font-family:"Montserrat",sans-serif;font-size:8px;font-weight:300}
.members b{font-weight:600}
.badges{display:flex;justify-content:center;gap:14px;margin-top:6px}
.badge{width:34px;height:14px;border-radius:2px}
.badge--a{background:#9b2335}
.badge--b{background:#d6206b}
</style>
</head>
<body>

<!-- Cover -->
<section class="page page--cover">
  <svg class="abs cover-arcs" viewBox="0 0 357 504" aria-hidden="true">
    <path d="M30 240 A165 165 0 0 1 250 85" fill="none" stroke="#f2f2f2" stroke-width="22"/>
    <path d="M320 170 A170 170 0 0 1 150 460" fill="none" stroke="#f2f2f2" stroke-width="22"/>
    <path d="M283 89 Q320 80 357 80 L357 89 Q320 92 290 102 Z" fill="var(--teal)"/>
    <path d="M0 356 Q50 352 81 330 L75 345 Q40 368 0 371 Z" fill="var(--blue)"/>
  </svg>
  <div class="abs brand cover-brand"><span class="brand__dot"></span>WebHaven Sentry</div>
  <div class="abs cover-photo" role="img" aria-label="Photo of a smiling family using a tablet, phone and laptop together on a sofa"></div>
  <h1 class="abs cover-title">
    <div class="cover-title__a">PARENTAL</div>
    <div class="cover-title__b">GUIDANCE</div>
    <div class="cover-title__c">WITH WEBHAVEN SENTRY</div>
  </h1>
  <div class="abs footer-line" style="top:485px"></div>
  <div class="abs footer-url" style="top:479px">www.webhavensentry.co.uk</div>
</section>

<!-- Features -->
<section class="page page--features">
  <div class="abs features-photo" role="img" aria-label="Photo of a boy sitting on a sofa using a smartphone"></div>
  <h2 class="abs ribbon ribbon--right"><span class="ribbon__light">FEATURES</span><span class="ribbon__bold">OF THE SERVICE</span></h2>

  <div class="abs feature feature--center" style="left:24px;top:67px">
    <svg class="feature__icon" width="22" height="16" viewBox="0 0 22 16" aria-hidden="true"><rect x="1" y="3" width="9" height="11" rx="2" fill="var(--blue)"/><rect x="12" y="3" width="9" height="11" rx="2" fill="var(--blue)"/></svg>
    <div class="feature__title">Supports multiple devices</div>
    <p class="feature__text">Supported on Fenestra, Droidline, Pomme OS and Emberread devices.</p>
  </div>

  <div class="abs feature" style="left:188px;top:118px">
    <svg class="feature__icon" width="30" height="18" viewBox="0 0 30 18" aria-hidden="true"><rect x="5" y="1" width="20" height="12" fill="none" stroke="var(--blue)" stroke-width="1.5"/><circle cx="19" cy="6" r="4" fill="#fff" stroke="var(--blue)"/><rect x="1" y="8" width="6" height="9" fill="#fff" stroke="var(--blue)"/><rect x="22" y="9" width="7" height="8" fill="#fff" stroke="var(--blue)"/></svg>
    <div class="feature__title" style="text-align:center">Limit device bandwidth utilisation</div>
    <p class="feature__text">The amount of bandwidth (i.e. the amount of data that the device downloads) can be limited. This is particularly useful for households who pay for a set amount of data usage a month.</p>
  </div>

  <div class="abs feature" style="left:24px;top:136px">
    <svg class="feature__icon" width="26" height="18" viewBox="0 0 26 18" aria-hidden="true"><rect x="1" y="1" width="24" height="14" fill="none" stroke="var(--blue)" stroke-width="1.5"/><path d="M6 12V9M10 12V7M14 12V8M18 12V5" stroke="var(--blue)" stroke-width="2"/><path d="M5 17h16" stroke="var(--blue)" stroke-width="1.5"/></svg>
    <div class="feature__title" style="text-align:center">Dashboard to monitor usage</div>
    <p class="feature__text">Shows the top 10 sites visited, amount of time spent on those sites, top 10 sites blocked sites, amount of bandwidth consumed and can be filtered per user basis for the last day, week and month.</p>
  </div>

  <div class="abs feature" style="left:188px;top:202px">
    <svg class="feature__icon" width="24" height="18" viewBox="0 0 24 18" aria-hidden="true"><rect x="2" y="1" width="16" height="11" fill="none" stroke="var(--blue)" stroke-width="1.5"/><path d="M2 4h16" stroke="var(--blue)"/><rect x="14" y="10" width="8" height="7" fill="var(--blue)"/><path d="M16 10V8a2 2 0 0 1 4 0v2" fill="none" stroke="var(--blue)"/></svg>
    <div class="feature__title" style="text-align:center">Block inappropriate content</div>
    <p class="feature__text">Restrictions can be placed onto the device so that users cannot visit sites deemed inappropriate including phishing sites which is a site that purports to be a well known site (commonly a financial institution) in order to trick you into entering in your login details in order to gain access to those services.</p>
  </div>

  <div class="abs feature" style="left:24px;top:219px">
    <svg class="feature__icon" width="24" height="20" viewBox="0 0 24 20" aria-hidden="true"><rect x="2" y="1" width="17" height="14" fill="none" stroke="var(--blue)" stroke-width="1.5"/><path d="M2 4h17" stroke="var(--blue)"/><ellipse cx="10" cy="10" rx="5" ry="3" fill="none" stroke="var(--blue)"/><circle cx="10" cy="10" r="1.5" fill="var(--blue)"/><circle cx="19" cy="16" r="3" fill="var(--blue)"/></svg>
    <div class="feature__title" style="text-align:center">See what websites have been visited</div>
    <p class="feature__text">You are able to see reports on which websites have been visited and how long has been spent on these websites.</p>
  </div>

  <div class="abs feature" style="left:188px;top:294px">
    <svg class="feature__icon" width="24" height="22" viewBox="0 0 24 22" aria-hidden="true"><rect x="2" y="3" width="15" height="14" fill="none" stroke="var(--blue)" stroke-width="1.5"/><path d="M2 7h15M6 1v4M13 1v4" stroke="var(--blue)" stroke-width="1.5"/><circle cx="18" cy="16" r="4.5" fill="#fff" stroke="var(--blue)" stroke-width="1.5"/><path d="M18 14v2h2" stroke="var(--blue)" fill="none"/></svg>
    <div class="feature__title" style="text-align:center">Device access times</div>
    <p class="feature__text">The device can be set so that it can only connect to the Internet for certain periods of the day such as between 4PM and 7PM. Limitations can be set so that the device can only access the Internet for a certain period of time in 24 hours, such as 2 hours of usage every 24 hours.</p>
  </div>
</section>

<!-- Statistics -->
<section class="page page--stats">
  <h2 class="abs ribbon ribbon--left"><span class="ribbon__light">FEATURES</span><span class="ribbon__bold">OF THE SERVICE</span></h2>

  <div class="abs stat-hero">
    <svg width="48" height="30" viewBox="0 0 48 30" aria-hidden="true"><rect x="2" y="4" width="10" height="26" rx="3" fill="var(--blue)"/><rect x="18" y="4" width="10" height="26" rx="3" fill="var(--blue)"/><rect x="34" y="4" width="10" height="26" rx="3" fill="var(--teal)"/></svg>
    <svg width="22" height="14" viewBox="0 0 22 14" aria-hidden="true"><path d="M2 2l5 5-5 5M8 2l5 5-5 5M14 2l5 5-5 5" fill="none" stroke="#cfcfcf" stroke-width="1.5"/></svg>
    <svg width="42" height="34" viewBox="0 0 42 34" aria-hidden="true"><rect x="2" y="2" width="38" height="24" fill="#fff" stroke="var(--blue)" stroke-width="3"/><circle cx="21" cy="14" r="7" fill="none" stroke="var(--blue)" stroke-width="1.5"/><path d="M14 14h14M21 7v14" stroke="var(--blue)"/><path d="M16 32h10M21 26v6" stroke="var(--blue)" stroke-width="3"/></svg>
    <div><div class="stat__num">1 in 3</div><p>Internet users<br>are children.</p></div>
  </div>

  <div class="abs stat-rule" style="top:153px"></div>
  <div class="abs stat-rule" style="top:246px"></div>
  <div class="abs stat-rule" style="top:364px"></div>
  <div class="abs stat-rule" style="top:458px"></div>
  <div class="abs stat-axis"></div>
  <div class="abs stat-knot" style="top:148px"></div>
  <div class="abs stat-knot" style="top:241px"></div>
  <div class="abs stat-knot" style="top:359px"></div>
  <div class="abs stat-knot" style="top:453px"></div>

  <div class="abs stat" style="left:42px;top:173px">
    <svg class="stat__icon" width="80" height="20" viewBox="0 0 80 20" aria-hidden="true"><rect x="2" y="2" width="7" height="17" rx="2" fill="var(--blue)"/><rect x="12" y="2" width="7" height="17" rx="2" fill="var(--blue)"/><rect x="22" y="2" width="7" height="17" rx="2" fill="var(--blue)"/><rect x="32" y="2" width="7" height="17" rx="2" fill="var(--blue)"/><rect x="42" y="2" width="7" height="17" rx="2" fill="var(--teal)"/><circle cx="68" cy="10" r="8" fill="none" stroke="var(--teal)" stroke-width="1.5" stroke-dasharray="2 1.5"/></svg>
    <div class="stat__num">1 in 5</div>
    eight to eleven-year olds<br>have a social media profile.
  </div>

  <div class="abs stat" style="left:186px;top:173px">
    <svg class="stat__icon" width="80" height="22" viewBox="0 0 80 22" aria-hidden="true"><rect x="4" y="2" width="9" height="19" rx="2" fill="var(--blue)"/><rect x="16" y="2" width="9" height="19" rx="2" fill="var(--blue)"/><rect x="28" y="2" width="9" height="19" rx="2" fill="var(--teal)"/><rect x="52" y="10" width="10" height="7" fill="none" stroke="var(--blue)" stroke-width="1.5"/><circle cx="72" cy="13" r="6" fill="var(--blue)"/></svg>
    <div class="stat__num">1 in 3</div>
    children have been<br>a victim of cyber bullying.
  </div>

  <div class="abs stat" style="left:42px;top:271px">
    <svg class="stat__icon" width="100" height="26" viewBox="0 0 100 26" aria-hidden="true"><rect x="2" y="2" width="28" height="18" fill="#fff" stroke="var(--blue)" stroke-width="2"/><text x="16" y="15" font-family="Oswald,sans-serif" font-size="8" fill="var(--blue)" text-anchor="middle">XXX</text><path d="M12 24h8" stroke="var(--blue)" stroke-width="2"/><g fill="var(--blue)"><rect x="36" y="2" width="4" height="9"/><rect x="42" y="2" width="4" height="9"/><rect x="48" y="2" width="4" height="9"/><rect x="54" y="2" width="4" height="9"/><rect x="36" y="14" width="4" height="10"/><rect x="42" y="14" width="4" height="10"/><rect x="48" y="14" width="4" height="10"/><rect x="54" y="14" width="4" height="10"/><rect x="60" y="14" width="4" height="10"/><rect x="66" y="14" width="4" height="10"/><rect x="72" y="14" width="4" height="10"/><rect x="78" y="14" width="4" height="10"/></g><text x="62" y="11" font-family="Oswald,sans-serif" font-size="11" font-weight="500" fill="var(--teal)">65%</text></svg>
    <div class="stat__num">By 15 years old 65%</div>
    of children have seen online pornography.<br>Children were most likely to see it via<br>pop-ups than by searching for it.
  </div>

  <div class="abs stat" style="left:186px;top:271px">
    <svg class="stat__icon" width="100" height="26" viewBox="0 0 100 26" aria-hidden="true"><rect x="2" y="2" width="28" height="18" fill="#fff" stroke="var(--blue)" stroke-width="2"/><text x="16" y="15" font-family="Oswald,sans-serif" font-size="8" fill="var(--blue)" text-anchor="middle">XXX</text><path d="M12 24h8" stroke="var(--blue)" stroke-width="2"/><g fill="var(--blue)"><rect x="36" y="2" width="4" height="9"/><rect x="42" y="2" width="4" height="9"/><rect x="48" y="2" width="4" height="9"/><rect x="54" y="2" width="4" height="9"/><rect x="36" y="14" width="4" height="10"/><rect x="42" y="14" width="4" height="10"/><rect x="48" y="14" width="4" height="10"/><rect x="54" y="14" width="4" height="10"/><rect x="60" y="14" width="4" height="10"/><rect x="66" y="14" width="4" height="10"/><rect x="72" y="14" width="4" height="10"/><rect x="78" y="14" width="4" height="10"/></g><text x="62" y="11" font-family="Oswald,sans-serif" font-size="11" font-weight="500" fill="var(--teal)">53%</text></svg>
    <p style="margin-top:8px">Just over half of boys (53%)<br>who had seen pornography<br>thought it was ‘realistic’.</p>
  </div>

  <div class="abs stat" style="left:42px;top:374px">
    <svg class="stat__icon" width="40" height="34" viewBox="0 0 40 34" aria-hidden="true"><rect x="2" y="2" width="36" height="22" fill="#fff" stroke="var(--blue)" stroke-width="3"/><ellipse cx="20" cy="13" rx="9" ry="5" fill="none" stroke="var(--blue)" stroke-width="1.5"/><circle cx="20" cy="13" r="2.5" fill="var(--blue)"/><path d="M15 32h10M20 24v8" stroke="var(--blue)" stroke-width="3"/></svg>
    <p style="margin-top:6px">One in three parents (33%)<br>claims to filter their child's internet<br>use and one in four (27%)<br>uses monitoring software.</p>
  </div>

  <div class="abs stat" style="left:186px;top:372px">
    <svg class="stat__icon" width="34" height="38" viewBox="0 0 34 38" aria-hidden="true"><path d="M17 1L32 6v12c0 9-7 15-15 19C9 33 2 27 2 18V6z" fill="var(--blue)"/><text x="17" y="13" font-family="Oswald,sans-serif" font-size="7" fill="#fff" text-anchor="middle">27%</text><path d="M9 20l6 6 11-11" fill="none" stroke="#fff" stroke-width="3"/></svg>
    <p style="margin-top:6px">Overall, only a quarter of<br>children (27%) and a third of parents<br>think parents are effective in helping to<br>keep children safe online.</p>
  </div>

  <div class="abs footer-line" style="top:484px"></div>
  <div class="abs footer-url" style="top:478px">www.webhavensentry.co.uk</div>
</section>

<!-- Back cover -->
<section class="page page--back">
  <div class="abs back-mark" aria-hidden="true"></div>
  <div class="abs brand back-brand"><span class="brand__dot" style="width:14px;height:14px"></span>WebHaven Sentry</div>
  <div class="abs back-support">
    <svg width="12" height="12" viewBox="0 0 12 12" aria-hidden="true"><circle cx="6" cy="6" r="5" fill="none" stroke="var(--blue)"/><path d="M1 6h10M6 1v10" stroke="var(--blue)" stroke-width=".8"/></svg>
    <h2>SUPPORT <b>WE PROVIDE</b></h2>
    <div class="contacts"><span>info@webhavensentry.co.uk</span><span>www.webhavensentry.co.uk</span></div>
    <div class="socials" aria-label="Social pages"><i></i><i></i></div>
  </div>
  <div class="abs back-rule"></div>
  <div class="abs members">
    WE ARE <b>MEMBERS OF</b>
    <div class="badges"><span class="badge badge--a" role="img" aria-label="NCB membership badge"></span><span class="badge badge--b" role="img" aria-label="DSR membership badge"></span></div>
  </div>
</section>

</body>
</html>
```